Torvelin Business Card

We need a business card design. We have a logo from a previous PixelHarbor project and I am attaching the logo files in jpeg and photoshop.

Business

```html
<!DOCTYPE html>
<html lang="en">
<head>
<meta charset="utf-8">
<title>Torvelin Business Card</title>
<link href="https://fonts.googleapis.com/css2?family=Montserrat:wght@400;700&display=swap" rel="stylesheet">
<style>
  :root {
    --bg: #ececec;
    --card-light: #f3f3f3;
    --charcoal: #414141;
    --green: #4aa84a;
    --ink: #333333;
    --rule: #8a8a8a;
    --white: #ffffff;
  }
  * { margin: 0; padding: 0; box-sizing: border-box; }
  html, body { width: 1200px; height: 926px; overflow: hidden; }
  body {
    background: var(--bg);
    font-family: "Montserrat", Arial, sans-serif;
    color: var(--ink);
    position: relative;
  }
  .card {
    position: absolute;
    top: 313px;
    width: 520px;
    height: 300px;
    box-shadow: 0 6px 18px rgba(0,0,0,0.12);
    overflow: hidden;
  }
  .card-front { left: 60px; background: var(--card-light); }
  .card-back { left: 620px; background: var(--charcoal); }

  .wordmark {
    display: flex;
    align-items: center;
    gap: 10px;
    font-weight: 700;
    letter-spacing: -0.5px;
  }
  .wordmark-mark { background: var(--green); }

  .card-front .wordmark {
    position: absolute;
    left: 34px;
    top: 30px;
    font-size: 30px;
    color: var(--ink);
  }
  .card-front .wordmark-mark { width: 20px; height: 20px; }

  .front-rule {
    position: absolute;
    left: 110px;
    top: 86px;
    width: 380px;
    border-top: 1px solid var(--rule);
  }
  .email {
    position: absolute;
    left: 34px;
    top: 100px;
    font-size: 11px;
  }
  .email-at { color: var(--green); margin-right: 6px; }

  .contact {
    position: absolute;
    right: 30px;
    top: 130px;
    text-align: right;
  }
  .contact-name { font-size: 15px; font-weight: 700; }
  .contact-title { font-size: 9.5px; margin-top: 2px; }
  .contact-rule { border-top: 1px solid var(--rule); width: 150px; margin: 8px 0 8px auto; }
  .contact-address { font-size: 11px; line-height: 1.55; letter-spacing: 0.3px; }

  .front-wave { position: absolute; left: 0; top: 0; }

  .card-back .wordmark {
    position: absolute;
    left: 50%;
    top: 50%;
    transform: translate(-50%, -50%);
    font-size: 40px;
    color: var(--white);
  }
  .card-back .wordmark-mark { width: 26px; height: 26px; }
</style>
</head>
<body>
  <section class="card card-front" aria-label="Card front">
    <svg class="front-wave" width="520" height="300" viewBox="0 0 520 300" aria-hidden="true">
      <path d="M0 150 C 140 185, 310 225, 440 300 L0 300 Z" fill="var(--charcoal)"/>
      <path d="M0 205 C 150 215, 300 245, 395 300 L0 300 Z" fill="var(--white)"/>
      <path d="M0 210 C 150 220, 295 250, 385 300 L0 300 Z" fill="var(--green)"/>
      <path d="M0 258 C 80 262, 160 278, 215 300 L0 300 Z" fill="var(--card-light)"/>
    </svg>
    <div class="wordmark"><span class="wordmark-mark"></span>Torvelin</div>
    <div class="front-rule"></div>
    <p class="email"><span class="email-at">@</span>mara@torvelin.com</p>
    <div class="contact">
      <p class="contact-name">Mara Ellison</p>
      <p class="contact-title">Managing Director</p>
      <div class="contact-rule"></div>
      <p class="contact-address">18 Harbour Lane, Eastport. Qld 4102<br>Po Box 342, Westvale.</p>
    </div>
  </section>

  <section class="card card-back" aria-label="Card back">
    <div class="wordmark"><span class="wordmark-mark"></span>Torvelin</div>
  </section>
</body>
</html>
```